Web Design Project

I work in a sign company that print banners, back light films, and vinyl lettering. We also create metal store signs that lights up. We have a laser cutter that can cut plastics and a waterjet that can cut stainless steel.
Job: Create a homepage
Requirements:
1. Keep it simple and neat, I do not want it to be messy. (Similar to this website, plover, or this http://www.markelvo.example/)
2. A navigation bar that has (Will help if you show a template for one of these links):
-Home
-Signs
-Banners
-Lettering
-Prints
-Gallery
3.Bottom of the page
-Abous us
-Shipping and Returning Policy
-Resellers
4.Other (Somewhere easy to find)
-Login
-Shopping Cart
-Upload
Updates
Nice job designers. I am currently working on the Site's logo, so I will be posting that up later.
I would like you guys to change the selection on the navigation bar.
It should only have:
Banners
Lettering
Prints
Gallery
Keep up the good work
Sorry for the bad update, the Navigation bar should have:
Home
Signs
Banners
Lettering
Prints
Gallery

```html
<!DOCTYPE html>
<html lang="en">
<head>
<meta charset="utf-8">
<title>Tranova – Signs, Banners & Lettering</title>
<link href="https://fonts.googleapis.com/css2?family=Archivo+Black&family=Arimo:wght@400;700&family=Merriweather+Sans:wght@800&display=swap" rel="stylesheet">
<style>
:root{
  --ink:#1a1a1a;
  --text:#333;
  --muted:#666;
  --red:#a31616;
  --price:#b0141b;
  --dark:#3a3a3a;
  --darker:#222;
  --black:#000;
  --line:#c9c9c9;
  --panel:#fff;
  --page:#fff;
  --head-top:#f4f4f4;
  --head-bot:#dcdcdc;
}
*{box-sizing:border-box;margin:0;padding:0}
html,body{width:857px;height:1200px;overflow:hidden;background:var(--page)}
body{position:relative;font-family:"Arimo",Arial,sans-serif;color:var(--text);font-size:11px}
.abs{position:absolute}

/* header */
.site-header{left:0;top:0;width:857px;height:118px;background:linear-gradient(var(--head-top),var(--head-bot))}
.brand{left:38px;top:8px;font-family:"Archivo Black",Arial,sans-serif;font-size:56px;line-height:70px;color:var(--ink);letter-spacing:-1px}
.top-links{right:21px;top:12px;font-weight:700;font-size:11px;color:var(--ink)}
.utility{right:21px;top:42px;display:flex;gap:12px;align-items:center;font-size:11px;color:#444}
.utility span{display:flex;align-items:center;gap:4px}
.utility svg{width:22px;height:24px}

/* nav */
.main-nav{left:16px;top:88px;width:824px;height:30px;background:linear-gradient(#555,#2a2a2a);border-radius:3px 3px 0 0;display:flex;align-items:center}
.main-nav a{color:#fff;text-decoration:none;font-size:11px;height:30px;line-height:30px;text-align:center;border-right:1px solid #1c1c1c;box-shadow:inset -1px 0 0 #5e5e5e}
.nav-upload{position:absolute;left:594px;top:0;width:97px;height:30px;background:var(--red);display:flex;align-items:center;gap:8px;padding-left:10px;color:#fff;font-size:12px}
.nav-search{position:absolute;left:695px;top:6px;width:120px;height:18px;background:#fff;border-radius:3px;border:1px solid #999;font-size:9px;color:#999;padding-left:22px;line-height:16px}
.nav-search svg{position:absolute;left:7px;top:3px}

.black-band{left:0;top:118px;width:857px;height:282px;background:var(--black)}

/* side panels */
.panel{background:var(--panel);border:1px solid #999;border-radius:4px;overflow:hidden}
.panel-title{height:34px;background:linear-gradient(#6a6a6a,#3c3c3c);color:#fff;font-weight:700;font-size:13px;line-height:34px;padding-left:29px}
.products-menu{left:17px;top:126px;width:184px;height:257px}
.menu-select{height:30px;background:var(--red);padding:4px 6px}
.menu-select div{height:21px;background:#fff;border:1px solid #888;font-size:10px;line-height:19px;padding-left:10px;position:relative;color:#111}
.menu-select div b{position:absolute;right:0;top:0;width:26px;height:19px;background:linear-gradient(#eee,#bbb);border-left:1px solid #888}
.menu-list{list-style:none;padding:12px 0 0 35px;position:relative}
.menu-list li{font-size:10px;line-height:21.5px;color:#222}
.menu-scroll{position:absolute;right:10px;top:10px;width:4px;height:170px;background:#ddd}
.menu-scroll i{display:block;width:4px;height:30px;background:#777}

.hero{left:220px;top:127px;width:618px;height:257px;background:#fff;border-radius:8px;border:1px solid #ccc}
.hero-photo{position:absolute;left:15px;top:11px;width:587px;height:234px;background:linear-gradient(180deg,#d3d4d2 0%,#c8c9c7 60%,#9a9b98 100%)}
.hero-title{position:absolute;left:40px;top:33px;font-family:"Merriweather Sans",Arial,sans-serif;font-weight:800;font-size:25px;color:#111}

.partners{left:17px;top:411px;width:184px;height:245px}
.partner-grid{display:grid;grid-template-columns:1fr 1fr;gap:18px 10px;padding:16px 20px}
.partner-grid i{display:block;height:46px;background:#d7d7d7;border-radius:6px}
.partner-grid i:nth-child(odd){border-radius:50%;width:46px;margin:0 auto}

.newsletter{left:17px;top:669px;width:184px;height:54px;background:linear-gradient(#666,#3a3a3a)}
.newsletter .panel-title{height:30px;line-height:30px;background:none;padding-left:21px}
.newsletter-field{position:absolute;left:8px;top:28px;width:142px;height:19px;background:#fff;font-size:10px;color:#888;line-height:19px;padding-left:12px}
.newsletter-go{position:absolute;left:150px;top:28px;width:25px;height:19px;background:linear-gradient(#eee,#bbb);color:#111;font-size:10px;line-height:19px;text-align:center}

/* customizer */
.customizer{left:220px;top:410px;width:616px;height:702px;border:1px solid #aaa;border-radius:4px}
.section-bar{height:36px;background:linear-gradient(#4a4a4a,#2a2a2a);color:#fff;font-weight:700;font-size:13px;line-height:36px;padding-left:23px;border-radius:3px 3px 0 0}
.step{left:23px;top:50px;font-size:12px;color:#111}
.step em{font-style:normal;color:var(--red)}
.label{font-size:11px;color:#444}
.select{height:21px;background:linear-gradient(#fff,#e6e6e6);border:1px solid #bbb;border-radius:2px;font-size:8px;line-height:19px;padding-left:13px;color:#333}
.select::after{content:"";position:absolute;right:8px;top:7px;border:5px solid transparent;border-top:6px solid #333}
.num{width:22px;height:21px;border:1px solid #bbb;font-size:8px;line-height:19px;text-align:center;background:#fff}
.spin{width:8px;height:18px}
.divider{left:301px;top:80px;height:112px;border-left:1px dashed #999}
.price-label{left:318px;top:142px;font-size:11px;color:#444}
.price{left:318px;top:158px;font-size:19px;font-weight:700;color:var(--price)}
.update{left:397px;top:169px;font-size:8px;color:#555;text-decoration:underline}
.upload-btn{left:440px;top:160px;width:88px;height:22px;border:1px solid #999;border-radius:12px;background:linear-gradient(#fff,#ddd);font-size:11px;line-height:20px;padding-left:26px;color:#222}
.upload-btn svg{position:absolute;left:5px;top:4px}

.products-bar{left:0;top:222px;width:614px;height:29px;background:linear-gradient(#6a6a6a,#4a4a4a);color:#fff;font-size:13px;line-height:29px;padding-left:23px}
.products-bar span{position:absolute;right:17px;font-size:10px}
.tile{width:134px;height:131px;border:1px solid #ccc;border-radius:6px;background:#fff;box-shadow:0 1px 3px rgba(0,0,0,.15);text-align:center}
.tile div{width:111px;height:87px;margin:14px auto 8px}
.tile p{font-weight:700;font-size:10.5px;color:#222}

/* footer */
.footer-rule{left:0;top:1130px;width:857px;border-top:1px solid #ddd}
.footer-links{left:0;top:1142px;width:857px;text-align:center;font-size:10.5px;color:#555}
.footer-links a{color:var(--red);text-decoration:none}
.copyright{left:0;top:1172px;width:857px;height:28px;border-top:1px solid #e5e5e5;text-align:center;font-size:10.5px;color:#888;padding-top:6px}
.copyright b{font-weight:400;color:#222;margin-left:6px}
</style>
</head>
<body>

<header class="abs site-header"></header>
<div class="abs brand">Tranova</div>
<div class="abs top-links">Login | Help Center | 1.800.555.0142</div>
<div class="abs utility">
  <span><svg viewBox="0 0 22 24"><rect x="5" y="2" width="12" height="20" rx="2" fill="#333"/><rect x="7" y="4" width="8" height="4" fill="#ddd"/><g fill="#ddd"><rect x="7" y="10" width="2" height="2"/><rect x="10" y="10" width="2" height="2"/><rect x="13" y="10" width="2" height="2"/><rect x="7" y="14" width="2" height="2"/><rect x="10" y="14" width="2" height="2"/><rect x="13" y="14" width="2" height="2"/><rect x="7" y="18" width="2" height="2"/><rect x="10" y="18" width="2" height="2"/><rect x="13" y="18" width="2" height="2"/></g></svg>Pricing &amp; shipping</span>
  <span><svg viewBox="0 0 22 24"><rect x="8" y="2" width="6" height="12" rx="3" fill="#333"/><path d="M5 11a6 6 0 0 0 12 0M11 17v5M7 22h8" stroke="#333" stroke-width="1.6" fill="none"/></svg>Click to Chat</span>
  <span><svg viewBox="0 0 22 24"><rect x="2" y="5" width="15" height="14" fill="none" stroke="#333" stroke-width="1.6"/><path d="M5 9h9M5 12h9M5 15h6" stroke="#333" stroke-width="1.4"/><path d="M14 18l6-10" stroke="#333" stroke-width="2"/></svg>My Desing</span>
  <span><svg viewBox="0 0 22 24"><path d="M1 6h4l3 11h11l2-8H6" fill="none" stroke="#333" stroke-width="1.8"/><circle cx="9" cy="20" r="1.8" fill="#333"/><circle cx="17" cy="20" r="1.8" fill="#333"/></svg>Cart Items</span>
</div>

<nav class="abs main-nav">
  <a href="#" style="width:72px">Home</a>
  <a href="#" style="width:82px">Signs</a>
  <a href="#" style="width:89px">Banners</a>
  <a href="#" style="width:84px">Lettering</a>
  <a href="#" style="width:87px">Prints</a>
  <a href="#" style="width:85px">Gallery</a>
  <a href="#" style="width:95px;border:0;box-shadow:none">Support</a>
  <div class="nav-upload"><svg width="28" height="22" viewBox="0 0 28 22"><path d="M2 14l12-6 12 6-12 6z" fill="#ddd"/><path d="M2 14v3l12 5 12-5v-3l-12 6z" fill="#999"/><path d="M14 1l5 6h-3v5h-4V7H9z" fill="#f2c230"/></svg>Upload</div>
  <div class="nav-search"><svg width="9" height="10" viewBox="0 0 9 10"><circle cx="4" cy="4" r="3" fill="none" stroke="#888" stroke-width="1.3"/><path d="M6 6l2.5 3" stroke="#888" stroke-width="1.3"/></svg>Search</div>
</nav>

<div class="abs black-band"></div>

<aside class="abs panel products-menu">
  <div class="panel-title">Products</div>
  <div class="menu-select"><div>Letterring<b></b></div></div>
  <ul class="menu-list">
    <li>Car Lettering</li>
    <li>Car Window Lettering</li>
    <li>Die-Cut Decals</li>
    <li>Etched Glass Decals</li>
    <li>Store Window Lettering</li>
    <li>Store Window Lettering</li>
    <li>Store Window Lettering</li>
    <li>Store Window Lettering</li>
    <span class="menu-scroll"><i></i></span>
  </ul>
</aside>

<section class="abs hero">
  <div class="hero-photo" role="img" aria-label="White sports car with printed vinyl graphics parked against a grey wall"></div>
  <h1 class="hero-title">Printing banners</h1>
</section>

<aside class="abs panel partners">
  <div class="panel-title">Partners</div>
  <div class="partner-grid"><i></i><i></i><i></i><i></i><i></i><i></i></div>
</aside>

<aside class="abs panel newsletter">
  <div class="panel-title">Newsletter</div>
  <div class="newsletter-field">Your mail ID here</div>
  <div class="newsletter-go">Go</div>
</aside>

<main class="abs customizer">
  <div class="section-bar">Customize Your Product</div>
  <div class="abs step">Step : 1 <em>Product Detail and Design</em></div>

  <div class="abs label" style="left:23px;top:80px">Material :</div>
  <div class="abs select" style="left:23px;top:104px;width:118px">Vinyl Banner</div>
  <div class="abs label" style="left:23px;top:143px">Standard Size: [H x W]</div>
  <div class="abs select" style="left:23px;top:166px;width:118px">2' x 4' Feet</div>
  <div class="abs label" style="left:162px;top:143px">Custom Size: [Inches]</div>
  <div class="abs label" style="left:162px;top:170px">H</div>
  <div class="abs num" style="left:178px;top:166px">24</div>
  <svg class="abs spin" style="left:209px;top:168px" viewBox="0 0 8 18"><path d="M0 7l4-6 4 6zM0 11l4 6 4-6z" fill="#555"/></svg>
  <div class="abs label" style="left:232px;top:170px">W</div>
  <div class="abs num" style="left:248px;top:166px">48</div>
  <svg class="abs spin" style="left:279px;top:168px" viewBox="0 0 8 18"><path d="M0 7l4-6 4 6zM0 11l4 6 4-6z" fill="#555"/></svg>

  <div class="abs divider"></div>

  <div class="abs label" style="left:318px;top:80px">Options :</div>
  <div class="abs select" style="left:318px;top:104px;width:118px">Outdoor: <span style="color:var(--red)">+$5.98</span></div>
  <div class="abs label" style="left:465px;top:80px">Quantity :</div>
  <div class="abs num" style="left:468px;top:104px">1</div>
  <svg class="abs spin" style="left:497px;top:106px" viewBox="0 0 8 18"><path d="M0 7l4-6 4 6zM0 11l4 6 4-6z" fill="#555"/></svg>

  <div class="abs price-label">Price Ea.</div>
  <div class="abs price">$29.88</div>
  <div class="abs update">Update</div>
  <div class="abs upload-btn"><svg width="16" height="22" viewBox="0 0 16 22"><path d="M8 0l8 9h-5v13H5V9H0z" fill="#e9683c"/></svg>Upload file</div>

  <div class="abs products-bar">Products<span>View all</span></div>

  <div class="abs tile" style="left:20px;top:262px"><div role="img" aria-label="Woman beside a shop window with graphics" style="background:linear-gradient(135deg,#8a7c6a,#c9c0b2)"></div><p>Window Graphics</p></div>
  <div class="abs tile" style="left:169px;top:262px"><div role="img" aria-label="Assorted colourful campaign stickers" style="background:linear-gradient(135deg,#e0b52a,#3a5db0 60%,#c02a2a)"></div><p>Stickers</p></div>
  <div class="abs tile" style="left:318px;top:262px"><div role="img" aria-label="Monogram vinyl lettering on a beige wall" style="background:linear-gradient(#d9cdb6,#b9a98c)"></div><p>Vinyl Lettering</p></div>
  <div class="abs tile" style="left:467px;top:262px"><div role="img" aria-label="Orange graphic poster" style="background:linear-gradient(135deg,#e07a1c,#f0d2a8)"></div><p>Posters</p></div>

  <div class="abs tile" style="left:20px;top:406px"><div role="img" aria-label="Tradesman car magnet sign on a dark van" style="background:linear-gradient(#2c3e5a,#1d2a3e)"></div><p>Car Magnets</p></div>
  <div class="abs tile" style="left:169px;top:406px"><div role="img" aria-label="Business graphics on a rear car window" style="background:linear-gradient(#9bb6d4,#26303c)"></div><p>Rear Window Graphics</p></div>
  <div class="abs tile" style="left:318px;top:406px"><div role="img" aria-label="Landscaping company lettering on a vehicle" style="background:linear-gradient(#2d4a63,#1a2430)"></div><p>Car Lettering</p></div>
  <div class="abs tile" style="left:467px;top:406px"><div role="img" aria-label="Close-up of yellow and black die-cut decal" style="background:linear-gradient(135deg,#e8e8e8,#d8c318 60%,#111)"></div><p>Die-Cut Decals</p></div>

  <div class="abs tile" style="left:20px;top:549px"><div role="img" aria-label="Purple promotional magnet with a navigation device" style="background:linear-gradient(#6a4a98,#3c2a62)"></div><p>Car Magnets</p></div>
  <div class="abs tile" style="left:169px;top:549px"><div role="img" aria-label="Collage of colourful badge designs" style="background:linear-gradient(135deg,#d2352a,#f1d030 50%,#2f8ad0)"></div><p>Rear Window Graphics</p></div>
  <div class="abs tile" style="left:318px;top:549px"><div role="img" aria-label="Colourful typographic lettering artwork" style="background:linear-gradient(135deg,#7fb24a,#f0e6c8 50%,#e0533a)"></div><p>Car Lettering</p></div>
  <div class="abs tile" style="left:467px;top:549px"><div role="img" aria-label="Black typographic die-cut decal on cream" style="background:linear-gradient(#efe6c8,#2a2a2a)"></div><p>Die-Cut Decals</p></div>
</main>

<div class="abs footer-rule"></div>
<footer class="abs footer-links">
  <a href="#">home</a> &nbsp;|&nbsp; <a href="#">banner</a> &nbsp;|&nbsp; <a href="#">backlight film</a> &nbsp;|&nbsp; <a href="#">vinyl</a> &nbsp;|&nbsp; <a href="#">pcb poster</a> &nbsp;|&nbsp; <a href="#">custom works</a> &nbsp;|&nbsp; <a href="#">support</a> &nbsp;|&nbsp; <a href="#">Abous us</a> &nbsp;|&nbsp; <a href="#">Shipping and Returning Policy</a> &nbsp;|&nbsp; <a href="#">Resellers</a>
</footer>
<div class="abs copyright">Copyright © 2012 tranova. All rights reserved. <b>Terms of Use | Privacy Policy</b></div>

</body>
</html>
```